Torven Medical needs bold attention catching website for healthcare professionals(target)

I need a hero page as well as a products and about page for a website of mine. I specialize in orthopedic instruments . Specifically bone drills and saws. This whole company was founded to bring superb quality highly discounted medical instruments. Specifically bone drills, bone saws, k-wires and pins. Two main points should be cost savings and superior quality.

Target Market(s)

healthcare professionals Surgeons and hospital material managers

Number of Pages Required

3 page

Font styles to use
Serif

Colors

Designer to choose colors to be used in the design.

Requirements
Must have
• colors should match logo design

```html
<!DOCTYPE html>
<html lang="en">
<head>
<meta charset="utf-8">
<title>Torven Medical</title>
<link href="https://fonts.googleapis.com/css2?family=Merriweather:wght@400;700&family=Open+Sans:wght@400;600&display=swap" rel="stylesheet">
<style>
:root{
  --orange:#f7931e;
  --ink:#1f1f1f;
  --text:#222;
  --muted:#7a7a7a;
  --ring:#ececec;
  --band:#efefef;
  --field:#e6e6e6;
  --footer:#1c1c1c;
  --white:#fff;
  --steel:#bdbdbd;
  --steel-soft:rgba(205,205,205,.55);
  --gold-soft:rgba(214,179,122,.6);
}
*{margin:0;padding:0;box-sizing:border-box}
html,body{width:1200px;height:2880px;overflow:hidden;background:var(--white)}
body{position:relative;font-family:"Merriweather",Georgia,serif;color:var(--text)}
.abs{position:absolute}
.sans{font-family:"Open Sans",Arial,sans-serif}

/* hero */
.hero-bg{left:0;top:0;width:1200px;height:660px;background:radial-gradient(ellipse at 20% 30%,#fbfbfb 0%,#f1f1f1 45%,#e9e9e9 100%)}
.hero-cut{left:0;top:560px}
.logo{font-weight:700;font-size:20px;color:var(--ink);letter-spacing:.3px}
.nav a{position:absolute;top:48px;font-size:12px;font-weight:700;color:var(--ink);text-decoration:none}
.nav a.active{color:var(--orange)}
.nav a.active::after{content:"";position:absolute;left:0;right:0;top:24px;height:2px;background:var(--orange);width:20px;margin:auto}
.hero-title{left:173px;top:240px;font-size:25px;line-height:46px;font-weight:400;color:var(--ink)}
.hero-title .bar{position:absolute;left:0;top:40px;width:56px;height:3px;background:var(--orange)}
.save{left:173px;top:340px;font-size:15px;font-weight:700;color:var(--ink);display:flex;align-items:baseline;gap:10px}
.save b{font-size:29px;color:var(--orange)}
.btn{position:absolute;display:flex;align-items:center;justify-content:center;gap:12px;border-radius:20px;font-weight:700;font-size:13px;color:var(--white);background:var(--ink)}
.btn.orange{background:var(--orange)}
.hero-ring{left:620px;top:148px;width:392px;height:392px;border-radius:50%;border:38px solid var(--ink);background:var(--white);box-shadow:0 14px 30px rgba(0,0,0,.2)}
.hero-img{left:770px;top:165px;width:100px;height:360px;background:linear-gradient(90deg,transparent 0%,var(--steel-soft) 12%,transparent 28%,transparent 72%,var(--gold-soft) 84%,transparent 96%)}
.next{left:898px;top:424px;font-size:12px;font-weight:700;color:var(--ink)}
.dots span{position:absolute;top:572px;width:7px;height:7px;border-radius:50%;background:#cfcfcf}

/* sections */
.heading{font-size:25px;font-weight:700;color:var(--ink)}
.underline{height:3px;background:var(--orange);width:49px}
.ring{position:absolute;width:166px;height:166px;border-radius:50%;border:16px solid var(--ring);background:var(--white)}
.ring.dark{border-color:var(--ink)}
.thumb{position:absolute;background:radial-gradient(ellipse at 50% 50%,#c4c4c4 0%,rgba(205,205,205,.65) 40%,rgba(230,230,230,0) 72%)}
.thumb.bar{background:linear-gradient(180deg,transparent 0%,var(--steel) 50%,transparent 100%)}
.thumb.pin{background:linear-gradient(90deg,transparent 0%,var(--steel-soft) 20%,transparent 40%,transparent 60%,var(--gold-soft) 75%,transparent 90%)}
.pname{position:absolute;width:180px;text-align:center;font-size:12.5px;font-weight:700;color:#666;line-height:21px;letter-spacing:.3px}
.price{position:absolute;width:180px;text-align:center;font-size:11px;color:#777;letter-spacing:.5px}

.band{left:0;top:1649px;width:1200px;height:481px;background:var(--band)}
.photo-ring{left:171px;top:1714px;width:346px;height:346px;border-radius:50%;background:#e6e6e6}
.photo{left:194px;top:1737px;width:300px;height:300px;border-radius:50%;background:linear-gradient(180deg,#f6f6f6 0%,#e4d3c8 40%,#4a4a4a 72%,#2a2a2a 100%)}
.about-text{left:613px;top:1806px;width:415px;font-size:12px;line-height:24px;color:var(--muted)}
.about-text strong{color:var(--ink);font-weight:600}
.about-text p+p{margin-top:24px}
.vline{width:1px;background:var(--orange)}

.field{position:absolute;border:1px solid var(--field);background:var(--white);font-size:11px;color:#b3b3b3;padding:7px 12px;box-shadow:0 1px 3px rgba(0,0,0,.04)}

.footer{left:0;top:2615px;width:1200px;height:265px;background:var(--footer)}
.f-head{font-size:13px;font-weight:700;color:var(--white)}
.f-link{font-size:9.5px;color:var(--white)}
.f-link.active{color:var(--orange)}
.social{position:absolute;top:2746px;width:26px;height:26px;border-radius:50%;background:var(--white)}
.social.orange{background:var(--orange)}
.card{position:absolute;top:2648px;width:33px;height:19px;border-radius:2px}
</style>
</head>
<body>

<div class="abs hero-bg" role="img" aria-label="Soft white abstract fabric backdrop"></div>
<svg class="abs hero-cut" width="1200" height="110" viewBox="0 0 1200 110"><path d="M0 10 Q600 110 1200 10 L1200 110 L0 110Z" fill="#fff"/></svg>

<div class="abs logo" style="left:173px;top:46px">Torven Medical</div>
<nav class="nav">
  <a class="active" style="left:610px">Home</a>
  <a style="left:704px">Products</a>
  <a style="left:806px">Contact Us</a>
</nav>
<svg class="abs" style="left:976px;top:46px" width="18" height="18" viewBox="0 0 18 18"><circle cx="7" cy="7" r="5.5" fill="none" stroke="#f7931e" stroke-width="1.6"/><path d="M11 11l5 5" stroke="#f7931e" stroke-width="1.6"/></svg>
<svg class="abs" style="left:1011px;top:44px" width="16" height="19" viewBox="0 0 16 19"><rect x="1" y="6" width="14" height="12" rx="1" fill="none" stroke="#f7931e" stroke-width="1.6"/><path d="M5 8V4a3 3 0 0 1 6 0v4" fill="none" stroke="#f7931e" stroke-width="1.6"/></svg>

<h1 class="abs hero-title">High-Quality Products at a<br>Significantly Lower Cost<span class="bar"></span></h1>
<div class="abs save">save up to <b>50%-60%</b></div>
<div class="btn" style="left:174px;top:404px;width:145px;height:37px">Shop Now
  <svg width="26" height="6" viewBox="0 0 26 6"><path d="M0 3h24M21 0l4 3-4 3" fill="none" stroke="#fff" stroke-width="1.2"/></svg></div>

<div class="abs hero-ring"></div>
<div class="abs hero-img" role="img" aria-label="Surgical pin and gold drill bit"></div>
<div class="abs next">Next</div>
<svg class="abs" style="left:934px;top:427px" width="44" height="10" viewBox="0 0 44 10"><path d="M0 5h40M36 1l5 4-5 4" fill="none" stroke="#f7931e" stroke-width="1.4"/></svg>
<div class="dots"><span style="left:793px;background:var(--orange)"></span><span style="left:816px"></span><span style="left:835px"></span></div>

<div class="abs" style="left:571px;top:550px;width:58px;height:58px;border-radius:50%;border:1px solid #e2e2e2;background:#fff"></div>
<div class="abs" style="left:579px;top:558px;width:42px;height:42px;border-radius:50%;border:1px solid #cfcfcf;background:#fff"></div>
<svg class="abs" style="left:594px;top:569px" width="12" height="19" viewBox="0 0 12 19"><rect x="1" y="1" width="10" height="17" rx="5" fill="none" stroke="#1f1f1f" stroke-width="1.3"/><path d="M6 5v4" stroke="#1f1f1f" stroke-width="1.3"/></svg>
<div class="abs vline" style="left:600px;top:604px;height:62px"></div>

<h2 class="abs heading" style="left:0;width:1200px;text-align:center;top:718px">Products</h2>
<div class="abs underline" style="left:576px;top:757px"></div>

<div class="ring dark" style="left:188px;top:826px"></div>
<div class="thumb pin" role="img" aria-label="Surgical pin and gold drill bit" style="left:246px;top:810px;width:50px;height:200px"></div>
<div class="btn orange" style="left:199px;top:1048px;width:144px;height:37px">Buy Now</div>

<div class="ring" style="left:408px;top:826px"></div>
<div class="thumb bar" role="img" aria-label="Drill bit" style="left:404px;top:903px;width:172px;height:10px"></div>
<div class="pname" style="left:401px;top:1043px">Product Title Here</div>
<div class="price" style="left:401px;top:1072px">$25.00</div>

<div class="ring" style="left:627px;top:826px"></div>
<div class="thumb bar" role="img" aria-label="Intramedullary nail" style="left:620px;top:893px;width:180px;height:14px"></div>
<div class="pname" style="left:620px;top:1045px">Intramedullary Nail<br>Femur</div>
<div class="price" style="left:620px;top:1094px">$5.00-$35.00</div>

<div class="ring" style="left:845px;top:826px"></div>
<div class="thumb" role="img" aria-label="Bone drill" style="left:850px;top:862px;width:146px;height:138px"></div>
<div class="pname" style="left:838px;top:1045px">Bone Drill</div>
<div class="price" style="left:838px;top:1072px">$5.00-$35.00</div>

<div class="ring" style="left:188px;top:1180px"></div>
<div class="thumb" role="img" aria-label="Oscillating saw" style="left:204px;top:1214px;width:136px;height:110px"></div>
<div class="pname" style="left:181px;top:1398px">Oscillating Saw</div>
<div class="price" style="left:181px;top:1426px">$5.00-$35.00</div>

<div class="ring" style="left:408px;top:1180px"></div>
<div class="thumb bar" role="img" aria-label="Drill bit" style="left:404px;top:1257px;width:172px;height:10px"></div>
<div class="pname" style="left:401px;top:1397px">Product Title here</div>
<div class="price" style="left:401px;top:1426px">$25.00</div>

<div class="ring" style="left:627px;top:1180px"></div>
<div class="thumb" role="img" aria-label="Pair of electric oscillating saws" style="left:622px;top:1214px;width:176px;height:100px"></div>
<div class="pname" style="left:620px;top:1398px">Electric Oscillating<br>Saw</div>
<div class="price" style="left:620px;top:1448px">$550.00</div>

<div class="ring" style="left:845px;top:1180px"></div>
<div class="thumb" role="img" aria-label="Bone drill" style="left:850px;top:1216px;width:146px;height:138px"></div>
<div class="pname" style="left:838px;top:1398px">Bone Drill</div>
<div class="price" style="left:838px;top:1426px">$5.00-$35.00</div>

<div class="btn" style="left:527px;top:1535px;width:146px;height:37px">View All</div>

<div class="abs band"></div>
<div class="abs photo-ring"></div>
<div class="abs photo" role="img" aria-label="Smiling medical professional in dark scrubs with arms crossed"></div>
<h2 class="abs heading" style="left:611px;top:1736px">About</h2>
<div class="abs underline" style="left:611px;top:1774px"></div>
<div class="abs about-text sans">
  <p><strong>Torven Medical</strong> was created to offer hospitals and physicians high-quality products at a significantly lower cost.</p>
  <p><strong>Torven Medical</strong> focus is on the orthopedic disposable market by providing quality generic products that are utilized to replace many legacy products thatt have low physician preference and are subject to 5%-10% annual unsustainable price increases.</p>
</div>
<div class="btn" style="left:610px;top:2001px;width:145px;height:37px">Read More</div>
<div class="abs vline" style="left:600px;top:2086px;height:90px"></div>

<h2 class="abs heading" style="left:0;width:1203px;text-align:center;top:2204px;font-weight:400">Send us a Message</h2>
<div class="field sans" style="left:381px;top:2264px;width:208px;height:28px">First Name</div>
<div class="field sans" style="left:610px;top:2264px;width:210px;height:28px">Last Name</div>
<div class="field sans" style="left:381px;top:2309px;width:208px;height:28px">Email</div>
<div class="field sans" style="left:610px;top:2309px;width:210px;height:28px">Phone</div>
<div class="field sans" style="left:381px;top:2353px;width:439px;height:130px">Message</div>
<div class="btn" style="left:381px;top:2502px;width:439px;height:37px">Send Message</div>

<div class="abs footer"></div>
<div class="abs logo" style="left:173px;top:2668px;color:var(--white)">Torven Medical</div>
<div class="abs f-head" style="left:392px;top:2645px">Info</div>
<div class="abs f-link sans active" style="left:392px;top:2677px">Home</div>
<div class="abs f-link sans" style="left:392px;top:2700px">About</div>
<div class="abs f-link sans" style="left:392px;top:2722px">Products</div>
<div class="abs f-link sans" style="left:392px;top:2744px">Contact</div>
<div class="abs f-head" style="left:611px;top:2645px">Connect</div>
<div class="abs f-link sans" style="left:611px;top:2677px">(555) 014-2290</div>
<div class="abs f-link sans" style="left:611px;top:2700px">info@torvenmedical.com</div>
<div class="social orange" style="left:611px"></div>
<div class="social" style="left:660px"></div>
<div class="social" style="left:708px"></div>
<div class="card" style="left:829px;background:#2f6db5"></div>
<div class="card" style="left:869px;background:#f2f2f2"></div>
<div class="card" style="left:909px;background:#4aa3df"></div>
<div class="card" style="left:949px;background:#f2f2f2"></div>
<div class="card" style="left:989px;background:#f2f2f2"></div>
<div class="abs f-link sans" style="left:171px;top:2828px">© 2019 TORVENMEDICAL</div>

</body>
</html>
```